Quimby's Yard & Garden Center Business Card Update

I need an updated Business card design for my Lawn and Garden Center. We do Landscaping installs, Lawn Mowing, Snow Removal and also have a Garden Center Retail Division. I uploaded a few of our previous business cards to give an idea of what we are starting with. The main goal of this update is to simplify and modernize the business card, not all of the services that are on the previous cards has to be on the new one but I would still like to highlight our main services. There is also a sample of our logo that Can be used in the design.

Industry/Entity Type

Landscaping

Contact Information for Business Card

Morris Quimby
Morris@Quimbysyardandgarden.example
Business (555) 201-7784
Cell (555) 318-6092

Colors

Designer to choose colors to be used in the design.

Requirements
Must have
• Services Provided :
• Landscaping
• Lawn Maintenance
• Snow Removal
• Garden Center

```html
<!DOCTYPE html>
<html lang="en">
<head>
<meta charset="utf-8">
<title>Quimby's Yard &amp; Garden Center – Business Card</title>
<link rel="stylesheet" href="https://fonts.googleapis.com/css2?family=Montserrat:wght@600;700&family=Open+Sans:wght@400;600;700&display=swap">
<style>
  :root {
    --bg: #2a2a2a;
    --ink: #0a0a0a;
    --green: #2e5229;
    --white: #ffffff;
    --name-green: #2e5229;
    --rule: #1a1a1a;
    --divider: #8a9a88;
  }
  * { box-sizing: border-box; margin: 0; padding: 0; }
  html, body { width: 1200px; height: 900px; overflow: hidden; }
  body {
    background: var(--bg);
    font-family: "Open Sans", sans-serif;
    position: relative;
  }
  .card {
    position: absolute;
    left: 250px;
    width: 700px;
    height: 400px;
    overflow: hidden;
    box-shadow: 0 10px 24px rgba(0,0,0,.45);
  }
  .card--back { top: 35px; background: var(--green); }
  .card--front { top: 465px; background: var(--white); }

  /* back */
  .back__top {
    position: absolute; inset: 0 0 auto 0; height: 165px;
    background: var(--ink);
    display: flex; align-items: center; justify-content: center;
  }
  .brand-name {
    font-family: "Open Sans", sans-serif;
    font-weight: 700;
    font-size: 64px;
    letter-spacing: 1px;
    line-height: 1;
  }
  .back__top .brand-name { color: var(--white); }
  .back__rule {
    position: absolute; left: 0; right: 0; top: 190px;
    border-top: 2px solid var(--rule);
  }
  .services {
    position: absolute; left: 0; right: 0; top: 215px;
    text-align: center;
  }
  .services__title {
    font-weight: 700; font-size: 16px; letter-spacing: 1px;
    color: var(--ink); margin-bottom: 14px;
  }
  .services__list { list-style: none; color: var(--white); font-size: 18px; line-height: 24px; letter-spacing: .5px; }

  /* front */
  .front__top {
    position: absolute; inset: 0 0 auto 0; height: 225px;
    background: var(--green);
    display: flex; flex-direction: column; align-items: center; justify-content: center;
    gap: 18px; padding-top: 10px;
  }
  .front__top .brand-name { color: var(--ink); }
  .tagline {
    font-weight: 700; font-size: 14px; letter-spacing: 1px; color: var(--ink);
  }
  .front__rule {
    position: absolute; left: 70px; right: 40px; top: 245px;
    border-top: 2px solid var(--rule);
  }
  .contact-block {
    position: absolute; left: 40px; right: 20px; top: 275px;
    display: flex; align-items: center;
  }
  .holder-name {
    font-family: "Montserrat", sans-serif;
    font-weight: 700; font-size: 28px; letter-spacing: 1px;
    color: var(--name-green);
    white-space: nowrap;
    flex: none;
    padding: 22px 20px 22px 0;
    border-right: 2px solid var(--divider);
    line-height: 1.2;
  }
  .contact-list { list-style: none; padding-left: 18px; font-size: 16px; color: var(--ink); line-height: 26px; }
  .contact-list li { display: flex; align-items: center; gap: 10px; white-space: nowrap; }
  .contact-list svg { width: 17px; height: 17px; flex: none; }
</style>
</head>
<body>
  <section class="card card--back" aria-label="Card back">
    <div class="back__top">
      <span class="brand-name">Quimby's</span>
    </div>
    <div class="back__rule"></div>
    <div class="services">
      <h2 class="services__title">SERVICES PROVIDED</h2>
      <ul class="services__list">
        <li>LANDSCAPING</li>
        <li>LAWN MAINTENANCE</li>
        <li>SNOW REMOVAL</li>
        <li>GARDEN CENTER</li>
      </ul>
    </div>
  </section>

  <section class="card card--front" aria-label="Card front">
    <div class="front__top">
      <span class="brand-name">Quimby's</span>
      <span class="tagline">QUIMBY'S YARD &amp; GARDEN CENTER</span>
    </div>
    <div class="front__rule"></div>
    <div class="contact-block">
      <h1 class="holder-name">MORRIS QUIMBY</h1>
      <ul class="contact-list">
        <li>
          <svg viewBox="0 0 20 20" fill="none" stroke="var(--green)" stroke-width="1.6"><circle cx="10" cy="10" r="8"/><path d="M7 6c0 4 3 7 7 7l1-2-2-1-1 1c-1-.5-2-1.5-2.5-2.5l1-1-1-2z"/></svg>
          (555) 201-7784
        </li>
        <li>
          <svg viewBox="0 0 20 20" fill="none" stroke="var(--green)" stroke-width="1.6"><rect x="6" y="2" width="8" height="16" rx="1.5"/><line x1="9" y1="15" x2="11" y2="15"/></svg>
          (555) 318-6092
        </li>
        <li>
          <svg viewBox="0 0 20 20" fill="none" stroke="var(--green)" stroke-width="1.6"><rect x="2" y="5" width="16" height="11"/><path d="M2 5l8 6 8-6"/></svg>
          Morris@Quimbysyardandgarden.example
        </li>
      </ul>
    </div>
  </section>
</body>
</html>
```